Business Card Design Project

Brightwater Advisory is a newly created boutique consultancy focussing on delivering strategic consulting to medium and large businesses, with a focus on:
- Strategic planning and execution.
- Corporate function optimisation, especially in the areas of finance, commercial, and IT. This includes implementing the right functional design for the needs of the business, and ensuring the right skills.
- Performance management, in particular project governance and control, operational metrics and management reporting.
I have in mind a tag line for the business being:
"Helping business to discover sustainable value."
I am looking for a letterhead design which utilises my new logo on report templates (powerpoint and word), and letterhead.
Lexipoint defines a mother lode as follows:
"Mother lode is a principal vein or zone of veins of gold or silver ore. The term probably came from a literal translation of the Spanish veta madre, a term common in old Mexican mining. Veta madre, for instance, is the name given to an 11-kilometre-long (6.8 mi) silver vein discovered in 1548 in Guanajuato, New Spain (modern-day Mexico)."
My preference is for black and gold. Logo files are attached in .eps format. All fonts are outlined. The fonts that are used are "Crimson Text" and "Josefin Sans". They are free open source fonts and they are available here: http://www.typevault-demo.net/fonts
Target Market(s)
Medium to large corporates.
Industry/Entity Type
Boutique
Other font styles liked:
- All Fonts Are Outlined. The Fonts That Are Used Are "Crimson Text" And "Josefin Sans". They Are Free Open Source Fonts And They Are Available Here: Http://www.typevault-demo.net/fonts

```html
<!DOCTYPE html>
<html lang="en">
<head>
<meta charset="utf-8">
<title>Brightwater Advisory – Business Card</title>
<link rel="stylesheet" href="https://fonts.googleapis.com/css2?family=Crimson+Text:wght@400&family=Josefin+Sans:wght@300;400&display=swap">
<style>
  :root {
    --ink: #050404;
    --paper: #ffffff;
    --gold: #dba520;
    --backdrop: #dcdcdc;
    --text-dark: #111111;
  }
  * { box-sizing: border-box; margin: 0; padding: 0; }
  html, body { width: 1200px; height: 1000px; overflow: hidden; }
  body { background: var(--backdrop); position: relative; font-family: "Crimson Text", Georgia, serif; }

  .card { position: absolute; left: 304px; width: 602px; height: 360px; overflow: hidden; }
  .card--front { top: 88px; background: var(--ink); }
  .card--back { top: 543px; background: var(--paper); }

  /* front */
  .front-mark { position: absolute; left: 234px; top: 45px; width: 134px; height: 135px; border: 9px solid var(--paper); }
  .front-name { position: absolute; left: 0; width: 100%; text-align: center; color: var(--paper); font-weight: 400; line-height: 1; }
  .front-name__main { top: 215px; font-size: 53px; letter-spacing: 1px; }
  .front-rule { position: absolute; left: 96px; top: 269px; width: 410px; height: 3px; background: var(--gold); }
  .front-name__sub { top: 281px; font-family: "Josefin Sans", Arial, sans-serif; font-weight: 300; font-size: 24px; letter-spacing: 9px; padding-left: 9px; }
  .tagline { position: absolute; top: 307px; left: 0; width: 100%; text-align: center; color: var(--paper);
             font-size: 8px; letter-spacing: 1px; line-height: 1; }

  /* back */
  .back-mark { position: absolute; left: 56px; top: 32px; width: 73px; height: 72px; border: 7px solid var(--ink); }
  .back-name { position: absolute; color: var(--ink); font-weight: 400; line-height: 1; }
  .back-name__main { left: 148px; width: 278px; text-align: center; top: 37px; font-size: 37px; letter-spacing: 1px; }
  .back-rule { position: absolute; left: 148px; top: 72px; width: 278px; height: 2px; background: var(--gold); }
  .back-name__sub { left: 148px; width: 278px; text-align: center; top: 80px; font-family: "Josefin Sans", Arial, sans-serif; font-weight: 300; font-size: 17px; letter-spacing: 6px; padding-left: 6px; }

  .person { position: absolute; left: 57px; top: 167px; }
  .person__name { font-size: 46px; line-height: 1; color: var(--text-dark); }
  .person__title { font-family: "Josefin Sans", Arial, sans-serif; font-weight: 400; font-size: 25px; margin-top: 14px; color: var(--text-dark); letter-spacing: 1px; }

  .contact { position: absolute; left: 389px; top: 163px; list-style: none; }
  .contact__item { display: flex; align-items: center; height: 34.5px; font-size: 15px; color: var(--text-dark); }
  .contact__item--web { font-size: 16px; }
  .contact__icon { width: 16px; height: 16px; margin-right: 9px; fill: var(--ink); }

  .wave { position: absolute; left: 0; top: 0; width: 602px; height: 360px; }
</style>
</head>
<body>

<section class="card card--front" aria-label="Card front">
  <div class="front-mark"></div>
  <div class="front-name front-name__main">BRIGHTWATER</div>
  <div class="front-rule"></div>
  <div class="front-name front-name__sub">ADVISORY</div>
  <p class="tagline">GUIDING COMPANIES TOWARD LASTING GROWTH TODAY</p>
</section>

<section class="card card--back" aria-label="Card back">
  <svg class="wave" viewBox="0 0 602 360" aria-hidden="true">
    <path d="M0 322 C100 292 220 330 340 340 C450 349 540 312 602 260 L602 360 L0 360 Z" fill="var(--ink)"/>
    <path d="M0 320 C100 290 220 328 340 338 C450 347 540 310 602 258" fill="none" stroke="var(--gold)" stroke-width="8"/>
  </svg>

  <div class="back-mark"></div>
  <div class="back-name back-name__main">BRIGHTWATER</div>
  <div class="back-rule"></div>
  <div class="back-name back-name__sub">ADVISORY</div>

  <div class="person">
    <div class="person__name">Name</div>
    <div class="person__title">TITLE</div>
  </div>

  <ul class="contact">
    <li class="contact__item">
      <svg class="contact__icon" viewBox="0 0 16 16"><path d="M8 1 L15 7 L13 7 L13 14 L3 14 L3 7 L1 7 Z"/></svg>
      Street 111
    </li>
    <li class="contact__item">
      <svg class="contact__icon" viewBox="0 0 16 16"><path d="M4 1 H12 A1 1 0 0 1 13 2 V14 A1 1 0 0 1 12 15 H4 A1 1 0 0 1 3 14 V2 A1 1 0 0 1 4 1 Z M5 3 V12 H11 V3 Z"/></svg>
      999 888 777
    </li>
    <li class="contact__item">
      <svg class="contact__icon" viewBox="0 0 16 16"><path d="M1 3 H15 V13 H1 Z M2 4.5 V5.2 L8 9 L14 5.2 V4.5 Z"/></svg>
      name@brightwater.org
    </li>
    <li class="contact__item contact__item--web">
      <svg class="contact__icon" viewBox="0 0 16 16"><circle cx="8" cy="8" r="6.5" fill="none" stroke="var(--ink)" stroke-width="1.4"/><ellipse cx="8" cy="8" rx="2.8" ry="6.5" fill="none" stroke="var(--ink)" stroke-width="1.2"/><path d="M1.5 8 H14.5 M2.5 4.8 H13.5 M2.5 11.2 H13.5" stroke="var(--ink)" stroke-width="1.1"/></svg>
      brightwater.com
    </li>
  </ul>
</section>

</body>
</html>
```